Business Card Design Project

I need a new business card for side business. Very simple and to the point. I am a licensed massage therapist and want the colors to be warm. I don't have a logo or company name. I just need to convey that I am a Licensed Massage Therapist and have my contact information so people can contact me. I'll attach some files that I like. I am a male so I don't want it to be feminine.

One file is my existing card. I like Tamsin's card and the layout so would prefer a similar layout. I would like to incorporate my swimmer/biker/runner image. Doesn't have to be the exact likeness because I don't have that file but something similar to that. I would like to also include my areas of specialty of: Swedish, Deep Tissue, Sports, and Hot Stone

I would also like to incorporate a QR code on the back of the card centered.
Updates

Payment is NOW guaranteed to the design I choose.  I updated my creative brief so hopefully it is more clear.  

Industry/Entity Type

Massage

Requirements
Must have
• Gavin Thrushwell
Licensed Massage Therapist
or
Massage Therapy
203-555-0187
gthrushwell@mailvale.net

```html
<!DOCTYPE html>
<html lang="en">
<head>
<meta charset="utf-8">
<title>Gavin Thrushwell – Licensed Massage Therapist</title>
<link rel="stylesheet" href="https://fonts.googleapis.com/css2?family=Raleway:ital,wght@0,300;0,400;1,300&display=swap">
<style>
  :root {
    --sand-light: #ebe2d3;
    --sand-mid: #d9ccb7;
    --sand-deep: #c2b39c;
    --disc: #333232;
    --ink-light: #f4f1ec;
    --rule: #cfcac2;
  }
  html, body {
    margin: 0;
    padding: 0;
    overflow: hidden;
    background: #ffffff;
  }
  .card {
    position: relative;
    width: 686px;
    height: 1200px;
    overflow: hidden;
    font-family: "Raleway", sans-serif;
  }
  .sand-texture {
    position: absolute;
    inset: 0;
    background:
      radial-gradient(circle at 50% 50%, var(--sand-light) 0%, var(--sand-mid) 55%, var(--sand-deep) 100%);
  }
  .emblem {
    position: absolute;
    left: 160px;
    top: 417px;
    width: 366px;
    height: 366px;
    border-radius: 50%;
    background: var(--disc);
    color: var(--ink-light);
    text-align: center;
  }
  .therapist-name {
    position: absolute;
    top: 100px;
    left: 0;
    right: 0;
    margin: 0;
    font-size: 29px;
    font-weight: 400;
    font-style: italic;
    letter-spacing: 3px;
    text-transform: uppercase;
  }
  .divider {
    position: absolute;
    left: 22px;
    right: 22px;
    height: 0;
    border-top: 2px solid var(--rule);
  }
  .divider--upper { top: 147px; }
  .divider--lower { top: 204px; }
  .credential {
    position: absolute;
    top: 163px;
    left: 0;
    right: 0;
    margin: 0;
    font-size: 21px;
    font-weight: 300;
    font-style: italic;
    letter-spacing: 0.5px;
  }
  .contact {
    position: absolute;
    top: 224px;
    left: 0;
    right: 0;
    margin: 0;
    font-size: 20px;
    font-weight: 300;
    font-style: italic;
    line-height: 26px;
  }
  .contact span { display: block; }
</style>
</head>
<body>
  <div class="card">
    <div class="sand-texture" role="img" aria-label="Raked sand with concentric ripple rings spreading out from the center"></div>
    <div class="emblem">
      <h1 class="therapist-name">Gavin Thrushwell</h1>
      <div class="divider divider--upper"></div>
      <p class="credential">Licensed Massage Therapist</p>
      <div class="divider divider--lower"></div>
      <p class="contact">
        <span class="contact-phone">203-555-0187</span>
        <span class="contact-email">gthrushwell@mailvale.net</span>
      </p>
    </div>
  </div>
</body>
</html>
```